Bright Path Flyer Design for Virtual Online Clinic. -5.5 x 8.5 inches (half sheet)

We need a clean, modern flyer design for Bright Path, a new virtual walk-in clinic based in British Columbia. The flyer will be used in libraries, pharmacies, and community centers to help residents easily access primary care through their Bright Path NFC access card.
The flyer will ask a question : NEED A DOCTOR? This should be large and attention grabbing.
The design should clearly feature a Bright Path card image (the access card) as the centerpiece and visually show how patients can use it to book appointments. The tone should feel trustworthy, healthcare-oriented, and community-friendly — clean fonts, clear spacing, and strong readability from a distance.

Side One: This card has the NFC Access Card.
NEED A DOCTOR? (Large Font, Attention Grabbing)
How to Book an Appointment using your Bright Path Card
Step 1: Tap Your Card on Your Phone
Hold your card near the back of your phone.
It will activate automatically — no app needed.
The Bright Path scheduler will open.
Step 2: Schedule Your Appointment
Select your clinical concern.
Choose your time window.
Register (only once).
Confirm your appointment.
Step 3: Relax, we’ll take care of the rest
A doctor will call during your scheduled time.
Once booked, you’ll be able to call our office.
No emails, no texts — just a real person.
It’s that simple.
Side Two:
About Bright Path
Created by Dr. Marcus Ferrigan
Bright Path was founded to make healthcare simple and convenient. Prescription renewals. Common infections. Medical notes. And so much more.
Our doctors can address 120+ health concerns virtually — providing quality care without the waiting room. No waiting rooms. Just real doctors providing real care.
Why Patients Choose Bright Path
Easy access – book and be seen from anywhere in BC.
Effortless booking – tap your Bright Path Card to begin.
Trusted physicians – every visit is with a licensed BC family doctor.
How It Works
Book your visit — choose a time window that fits your day.
Join the queue — you’ll be called when it’s your turn.
Speak directly with your doctor — simple, secure, and stress-free.
Convenient Care for Common Concerns

Additional Details.
Please find the domain to be launched soon. I've attached the NFC card file for review, it is 85.5 mm x 54 mm. The card will be glued to the flyer.
I've attached examples of flyers but they are not the look I am seeking and I am looking for creative solutions.
Thank you!
http://brightpath-example.test/

Adult Patients in British Columbia

Healthcare

• Looking for clean lines, uniform appearance, and high legibility i.e poppins

0054AA
0677BA
7BADD7
CADEEF
E8F1F8

• Need A Doctor?
• Elegant style, not too busy, clear layout.
• Clutter, look cheap - review examples.

```html
<!DOCTYPE html>
<html lang="en">
<head>
<meta charset="utf-8">
<title>Bright Path – Flyer</title>
<link href="https://fonts.googleapis.com/css2?family=Montserrat:wght@800;900&family=Poppins:wght@400;500;600;700&display=swap" rel="stylesheet">
<style>
  :root {
    --canvas: #e9e7ef;
    --paper: #ffffff;
    --brand-blue: #0054aa;
    --sky-blue: #7badd7;
    --aqua: #66e6e8;
    --ink: #16265a;
    --navy: #17234d;
    --photo-warm: #c9a88a;
    --photo-cool: #cfdbe6;
    --photo-soft: #d9cfc4;
  }
  * { margin: 0; padding: 0; box-sizing: border-box; }
  html, body { width: 1200px; height: 933px; overflow: hidden; }
  body { background: var(--canvas); font-family: "Poppins", sans-serif; color: var(--ink); position: relative; }

  .page { position: absolute; top: 22px; width: 575px; height: 889px; background: var(--paper); overflow: hidden; }
  .page--front { left: 18px; }
  .page--back { left: 607px; }

  .hero { position: absolute; left: 0; top: 0; width: 575px; background: var(--brand-blue); }
  .page--front .hero { height: 363px; border-bottom-right-radius: 64px; }
  .page--back .hero { height: 335px; border-bottom-right-radius: 48px; }

  .brand { position: absolute; color: #fff; font-family: "Poppins", sans-serif; font-weight: 500; font-size: 30px; letter-spacing: 0.5px; white-space: nowrap; }
  .page--front .brand { left: 29px; top: 62px; }
  .page--back .brand { left: 33px; top: 90px; }

  .headline { position: absolute; font-family: "Montserrat", sans-serif; font-weight: 900; white-space: nowrap; letter-spacing: -1px; }
  .headline span { display: block; }
  .headline .line-white { color: #fff; }
  .headline .line-sky { color: var(--sky-blue); }
  .page--front .headline { left: 28px; top: 133px; font-size: 82px; }
  .page--front .headline span { line-height: 58px; }
  .page--front .headline .line-sky { margin-top: 11px; }
  .page--back .headline { left: 29px; top: 147px; font-size: 70px; }
  .page--back .headline span { line-height: 50px; }
  .page--back .headline .line-sky { margin-top: 10px; }

  .subtitle { position: absolute; left: 30px; top: 270px; color: #fff; font-weight: 600; font-size: 20.5px; line-height: 29px; }
  .byline { position: absolute; left: 36px; top: 273px; color: #fff; font-weight: 600; font-size: 20.5px; }

  .step-band { position: absolute; left: 0; height: 42px; background: var(--aqua); border-radius: 0 21px 21px 0; display: flex; align-items: center; }
  .step-band .badge { position: absolute; left: 20px; top: 9px; width: 30px; height: 24px; }
  .step-band h2 { position: absolute; left: 66px; font-family: "Montserrat", sans-serif; font-weight: 900; font-size: 14.2px; letter-spacing: 0.8px; color: var(--ink); white-space: nowrap; }
  .step-band--three h2 { font-size: 13.7px; letter-spacing: -0.2px; }

  .section-band { position: absolute; left: 0; height: 41px; background: var(--aqua); border-radius: 0 21px 21px 0; }
  .section-band h2 { position: absolute; left: 31px; top: 7px; font-weight: 600; font-size: 18px; color: var(--ink); white-space: nowrap; }

  .checklist { list-style: none; }
  .checklist li { position: absolute; font-weight: 500; font-size: 14.5px; line-height: 17px; color: var(--ink); }
  .checklist li svg { position: absolute; width: 16px; height: 16px; top: 1px; }
  .page--front .checklist li { left: 55px; width: 345px; }
  .page--front .checklist li svg { left: -28px; }
  .page--back .checklist li { left: 62px; width: 505px; font-size: 14.3px; }
  .page--back .checklist li svg { left: -22px; }

  .photo-frame { position: absolute; background: var(--aqua); border-radius: 16px; padding: 9px; box-shadow: 0 6px 12px rgba(0, 40, 90, 0.18); }
  .photo-frame .photo { width: 100%; height: 100%; border-radius: 9px; }
  .photo--card { background: linear-gradient(135deg, #e9ddd0 0%, var(--photo-warm) 60%, #8e6a4c 100%); }
  .photo--calendar { background: linear-gradient(135deg, #f1f3f5 0%, var(--photo-cool) 100%); }
  .photo--rest { background: linear-gradient(135deg, #ece6df 0%, var(--photo-soft) 55%, #2c3346 100%); }

  .intro { position: absolute; left: 30px; width: 520px; font-weight: 400; font-size: 14.6px; line-height: 16.5px; color: var(--ink); }

  .contact-bar { position: absolute; left: 0; top: 792px; width: 575px; height: 97px; background: var(--navy); border-top-right-radius: 46px; color: #fff; }
  .contact-bar .phone { position: absolute; left: 54px; top: 30px; display: flex; align-items: center; gap: 10px; font-weight: 700; font-size: 21px; }
  .contact-bar .detail { position: absolute; left: 326px; display: flex; align-items: center; gap: 10px; font-size: 11.5px; font-weight: 400; }
  .contact-bar .detail--web { top: 18px; }
  .contact-bar .detail--address { top: 50px; }
</style>
</head>
<body>

<!-- Side one -->
<section class="page page--front">
  <div class="hero"></div>
  <div class="brand">Bright Path</div>
  <h1 class="headline"><span class="line-white">NEED A</span><span class="line-sky">DOCTOR?</span></h1>
  <p class="subtitle">How to Book an Appointment<br>using your Bright Path Card</p>

  <div class="step-band" style="top:345px; width:375px;">
    <svg class="badge" viewBox="0 0 30 24"><path d="M12 0 A12 12 0 1 0 12 24 C18 24 24 16 30 12 C24 8 18 0 12 0Z" fill="#2f5fd8"/><circle cx="12" cy="12" r="9" fill="#fff"/><text x="12" y="16.5" text-anchor="middle" font-family="Poppins, sans-serif" font-weight="700" font-size="12" fill="#16265a">1</text></svg>
    <h2>TAP YOUR CARD ON YOUR PHONE</h2>
  </div>
  <ul class="checklist">
    <li style="top:400px;"><svg viewBox="0 0 16 16"><circle cx="8" cy="8" r="8" fill="#66e6e8"/><path d="M4.5 8.3l2.4 2.3 4.6-4.8" stroke="#fff" stroke-width="1.8" fill="none" stroke-linecap="round" stroke-linejoin="round"/></svg>Hold your card near the back of your phone.</li>
    <li style="top:426px; width:300px;"><svg viewBox="0 0 16 16"><circle cx="8" cy="8" r="8" fill="#66e6e8"/><path d="M4.5 8.3l2.4 2.3 4.6-4.8" stroke="#fff" stroke-width="1.8" fill="none" stroke-linecap="round" stroke-linejoin="round"/></svg>It will activate automatically — no app needed.</li>
    <li style="top:468px;"><svg viewBox="0 0 16 16"><circle cx="8" cy="8" r="8" fill="#66e6e8"/><path d="M4.5 8.3l2.4 2.3 4.6-4.8" stroke="#fff" stroke-width="1.8" fill="none" stroke-linecap="round" stroke-linejoin="round"/></svg>The Bright Path scheduler will open.</li>
  </ul>

  <div class="step-band" style="top:503px; width:372px;">
    <svg class="badge" viewBox="0 0 30 24" style="left:18px;"><path d="M12 0 A12 12 0 1 0 12 24 C18 24 24 16 30 12 C24 8 18 0 12 0Z" fill="#2f5fd8"/><circle cx="12" cy="12" r="9" fill="#fff"/><text x="12" y="16.5" text-anchor="middle" font-family="Poppins, sans-serif" font-weight="700" font-size="12" fill="#16265a">2</text></svg>
    <h2 style="left:64px;">SCHEDULE YOUR APPOINTMENT</h2>
  </div>
  <ul class="checklist">
    <li style="top:558px; left:52px;"><svg viewBox="0 0 16 16"><circle cx="8" cy="8" r="8" fill="#66e6e8"/><path d="M4.5 8.3l2.4 2.3 4.6-4.8" stroke="#fff" stroke-width="1.8" fill="none" stroke-linecap="round" stroke-linejoin="round"/></svg>Select your clinical concern.</li>
    <li style="top:583px; left:52px;"><svg viewBox="0 0 16 16"><circle cx="8" cy="8" r="8" fill="#66e6e8"/><path d="M4.5 8.3l2.4 2.3 4.6-4.8" stroke="#fff" stroke-width="1.8" fill="none" stroke-linecap="round" stroke-linejoin="round"/></svg>Choose your time window.</li>
    <li style="top:608px; left:52px;"><svg viewBox="0 0 16 16"><circle cx="8" cy="8" r="8" fill="#66e6e8"/><path d="M4.5 8.3l2.4 2.3 4.6-4.8" stroke="#fff" stroke-width="1.8" fill="none" stroke-linecap="round" stroke-linejoin="round"/></svg>Register (only once).</li>
    <li style="top:633px; left:52px;"><svg viewBox="0 0 16 16"><circle cx="8" cy="8" r="8" fill="#66e6e8"/><path d="M4.5 8.3l2.4 2.3 4.6-4.8" stroke="#fff" stroke-width="1.8" fill="none" stroke-linecap="round" stroke-linejoin="round"/></svg>Confirm your appointment.</li>
  </ul>

  <div class="step-band step-band--three" style="top:668px; width:372px;">
    <svg class="badge" viewBox="0 0 30 24"><path d="M12 0 A12 12 0 1 0 12 24 C18 24 24 16 30 12 C24 8 18 0 12 0Z" fill="#2f5fd8"/><circle cx="12" cy="12" r="9" fill="#fff"/><text x="12" y="16.5" text-anchor="middle" font-family="Poppins, sans-serif" font-weight="700" font-size="12" fill="#16265a">3</text></svg>
    <h2 style="left:64px;">RELAX, WE’LL TAKE CARE OF THE REST</h2>
  </div>
  <ul class="checklist">
    <li style="top:723px; width:300px;"><svg viewBox="0 0 16 16"><circle cx="8" cy="8" r="8" fill="#66e6e8"/><path d="M4.5 8.3l2.4 2.3 4.6-4.8" stroke="#fff" stroke-width="1.8" fill="none" stroke-linecap="round" stroke-linejoin="round"/></svg>A doctor will call during your scheduled time.</li>
    <li style="top:765px; width:350px;"><svg viewBox="0 0 16 16"><circle cx="8" cy="8" r="8" fill="#66e6e8"/><path d="M4.5 8.3l2.4 2.3 4.6-4.8" stroke="#fff" stroke-width="1.8" fill="none" stroke-linecap="round" stroke-linejoin="round"/></svg>Once booked, you’ll be able to call our office.</li>
    <li style="top:791px;"><svg viewBox="0 0 16 16"><circle cx="8" cy="8" r="8" fill="#66e6e8"/><path d="M4.5 8.3l2.4 2.3 4.6-4.8" stroke="#fff" stroke-width="1.8" fill="none" stroke-linecap="round" stroke-linejoin="round"/></svg>No emails, no texts — just a real person.</li>
    <li style="top:815px;"><svg viewBox="0 0 16 16"><circle cx="8" cy="8" r="8" fill="#66e6e8"/><path d="M4.5 8.3l2.4 2.3 4.6-4.8" stroke="#fff" stroke-width="1.8" fill="none" stroke-linecap="round" stroke-linejoin="round"/></svg>It’s that simple.</li>
  </ul>

  <div class="photo-frame" style="left:391px; top:303px; width:150px; height:150px;">
    <div class="photo photo--card" role="img" aria-label="Photo of a hand tapping the Bright Path access card on a payment-style reader"></div>
  </div>
  <div class="photo-frame" style="left:397px; top:494px; width:144px; height:138px;">
    <div class="photo photo--calendar" role="img" aria-label="Photo of a person at a computer viewing an appointment calendar"></div>
  </div>
  <div class="photo-frame" style="left:398px; top:671px; width:150px; height:149px;">
    <div class="photo photo--rest" role="img" aria-label="Photo of a man relaxing on a sofa with hands behind his head"></div>
  </div>
</section>

<!-- Side two -->
<section class="page page--back">
  <div class="hero"></div>
  <div class="brand">Bright Path</div>
  <h1 class="headline"><span class="line-white">ABOUT</span><span class="line-sky">BRIGHT PATH</span></h1>
  <p class="byline">Created by Dr. Marcus Ferrigan</p>

  <p class="intro" style="top:350px;">Bright Path was founded to make healthcare simple and convenient. Prescription renewals. Common infections. Medical notes. And so much more.</p>
  <p class="intro" style="top:410px;">Our doctors can address 120+ health concerns virtually — providing quality care without the waiting room. No waiting rooms. Just real doctors providing real care.</p>

  <div class="section-band" style="top:471px; width:374px;"><h2>Why Patients Choose Bright Path</h2></div>
  <ul class="checklist">
    <li style="top:526px; left:62px;"><svg viewBox="0 0 16 16"><circle cx="8" cy="8" r="8" fill="#66e6e8"/><path d="M4.5 8.3l2.4 2.3 4.6-4.8" stroke="#fff" stroke-width="1.8" fill="none" stroke-linecap="round" stroke-linejoin="round"/></svg>Easy access – book and be seen from anywhere in BC.</li>
    <li style="top:553px; left:62px;"><svg viewBox="0 0 16 16"><circle cx="8" cy="8" r="8" fill="#66e6e8"/><path d="M4.5 8.3l2.4 2.3 4.6-4.8" stroke="#fff" stroke-width="1.8" fill="none" stroke-linecap="round" stroke-linejoin="round"/></svg>Effortless booking – tap your Bright Path Card to begin.</li>
    <li style="top:580px; left:62px;"><svg viewBox="0 0 16 16"><circle cx="8" cy="8" r="8" fill="#66e6e8"/><path d="M4.5 8.3l2.4 2.3 4.6-4.8" stroke="#fff" stroke-width="1.8" fill="none" stroke-linecap="round" stroke-linejoin="round"/></svg>Trusted physicians – every visit is with a licensed BC family doctor.</li>
  </ul>

  <div class="section-band" style="top:615px; width:381px;"><h2 style="left:38px;">How It Works</h2></div>
  <ul class="checklist">
    <li style="top:671px; left:69px;"><svg viewBox="0 0 16 16"><circle cx="8" cy="8" r="8" fill="#66e6e8"/><path d="M4.5 8.3l2.4 2.3 4.6-4.8" stroke="#fff" stroke-width="1.8" fill="none" stroke-linecap="round" stroke-linejoin="round"/></svg>Book your visit — choose a time window that fits your day.</li>
    <li style="top:698px; left:69px;"><svg viewBox="0 0 16 16"><circle cx="8" cy="8" r="8" fill="#66e6e8"/><path d="M4.5 8.3l2.4 2.3 4.6-4.8" stroke="#fff" stroke-width="1.8" fill="none" stroke-linecap="round" stroke-linejoin="round"/></svg>Join the queue — you’ll be called when it’s your turn.</li>
    <li style="top:725px; left:69px;"><svg viewBox="0 0 16 16"><circle cx="8" cy="8" r="8" fill="#66e6e8"/><path d="M4.5 8.3l2.4 2.3 4.6-4.8" stroke="#fff" stroke-width="1.8" fill="none" stroke-linecap="round" stroke-linejoin="round"/></svg>Speak directly with your doctor — simple, secure, and stress-free.</li>
    <li style="top:753px; left:69px;"><svg viewBox="0 0 16 16"><circle cx="8" cy="8" r="8" fill="#66e6e8"/><path d="M4.5 8.3l2.4 2.3 4.6-4.8" stroke="#fff" stroke-width="1.8" fill="none" stroke-linecap="round" stroke-linejoin="round"/></svg>Convenient Care for Common Concerns</li>
  </ul>

  <footer class="contact-bar">
    <div class="phone">
      <svg width="20" height="20" viewBox="0 0 20 20"><circle cx="10" cy="10" r="10" fill="#66e6e8"/><path d="M7.2 5.2c.4-.3.9-.2 1.1.2l1 1.8c.2.4.1.8-.2 1.1l-.7.6c.5 1.1 1.4 2 2.5 2.5l.6-.7c.3-.3.7-.4 1.1-.2l1.8 1c.4.2.5.7.2 1.1l-.8 1c-.4.5-1.1.6-1.7.4-2.6-.9-4.600-2.9-5.5-5.5-.2-.6-.1-1.3.4-1.7z" fill="#17234d"/></svg>
      +1-604-555-0142
    </div>
    <div class="detail detail--web">
      <svg width="18" height="18" viewBox="0 0 18 18"><circle cx="9" cy="9" r="9" fill="#66e6e8"/><rect x="4.5" y="5.8" width="9" height="6.4" rx="1" fill="#17234d"/><path d="M4.8 6.2L9 9.3l4.2-3.1" stroke="#66e6e8" stroke-width="1" fill="none"/></svg>
      brightpath-example.test
    </div>
    <div class="detail detail--address">
      <svg width="18" height="18" viewBox="0 0 18 18"><circle cx="9" cy="9" r="9" fill="#66e6e8"/><path d="M9 4a3.4 3.4 0 0 0-3.4 3.4C5.6 10 9 14 9 14s3.4-4 3.4-6.6A3.4 3.4 0 0 0 9 4z" fill="#17234d"/><circle cx="9" cy="7.4" r="1.2" fill="#66e6e8"/></svg>
      450 Harbour Ave., Vancouver
    </div>
  </footer>
</section>

</body>
</html>
```